Law Offices business card

Hi there, I'll need business card for the Law Offices of Colby Marchetti. The information must convey his strategic approach and quick resolution to complex business litigation needs. Please emphasize Civil Litigation, Corporate Law, Business Governance and Real Estate Law. Colby has over 25 years of experience in these fields.The card should be modern and edgy and the message should be clear. Please consult his current website for ideas.

```html
<!DOCTYPE html>
<html lang="en">
<head>
<meta charset="utf-8">
<title>Law Offices of Colby Marchetti – Business Card</title>
<link href="https://fonts.googleapis.com/css2?family=Old+Standard+TT:wght@400;700&family=Oswald:wght@400&display=swap" rel="stylesheet">
<style>
  :root {
    --backdrop: #e9e6e2;
    --card: #ffffff;
    --ink: #111111;
    --accent: #8e1b22;
    --edge: #d4d4d4;
  }
  * { box-sizing: border-box; margin: 0; padding: 0; }
  html, body { width: 1200px; height: 1200px; overflow: hidden; }
  body {
    background: var(--backdrop);
    position: relative;
    font-family: "Old Standard TT", Georgia, serif;
    color: var(--ink);
  }
  .card {
    position: absolute;
    left: 220px;
    width: 760px;
    height: 434px;
    background: var(--card);
    border: 1px solid var(--edge);
    box-shadow: 0 6px 18px rgba(0,0,0,0.12);
  }
  .card--back { top: 120px; }
  .card--front { top: 620px; }

  /* Back side */
  .practice-areas {
    position: absolute;
    left: 420px;
    top: 150px;
    font-weight: 700;
    font-size: 27px;
    line-height: 1.2;
  }

  /* Front side */
  .firm-mark {
    position: absolute;
    left: 40px;
    top: 80px;
    display: flex;
    align-items: flex-start;
    gap: 12px;
  }
  .firm-mark__square {
    width: 30px;
    height: 30px;
    background: var(--accent);
    margin-top: 30px;
    flex: none;
  }
  .firm-mark__name {
    font-weight: 700;
    font-size: 38px;
    line-height: 1.0;
    color: var(--ink);
  }
  .firm-mark__name small {
    display: block;
    font-size: 15px;
    letter-spacing: 0.04em;
    text-transform: uppercase;
    margin-bottom: 4px;
  }
  .divider {
    position: absolute;
    left: 380px;
    top: 60px;
    width: 3px;
    height: 280px;
    background: var(--accent);
  }
  .attorney {
    position: absolute;
    left: 410px;
    top: 62px;
  }
  .attorney__name {
    font-weight: 700;
    font-size: 36px;
    letter-spacing: 0.04em;
    white-space: nowrap;
  }
  .attorney__title {
    font-size: 11px;
    letter-spacing: 0.08em;
    text-align: center;
    margin-top: 2px;
  }
  .contact {
    list-style: none;
    margin-top: 20px;
    font-family: "Oswald", "Arial Narrow", sans-serif;
    font-size: 22px;
    line-height: 1.3;
    text-transform: uppercase;
    white-space: nowrap;
  }
  .contact__label { color: var(--accent); }
</style>
</head>
<body>
  <section class="card card--back" aria-label="Card back">
    <p class="practice-areas">Civil Litigation,<br>Corporate Law,<br>Business Governance,<br>Real Estate Law</p>
  </section>

  <section class="card card--front" aria-label="Card front">
    <div class="firm-mark">
      <span class="firm-mark__square"></span>
      <p class="firm-mark__name"><small>Law Offices of</small>Colby<br>Marchetti, PA</p>
    </div>
    <div class="divider"></div>
    <div class="attorney">
      <h1 class="attorney__name">Colby Marchetti</h1>
      <p class="attorney__title">ATTORNEY</p>
      <ul class="contact">
        <li><span class="contact__label">Phone:</span> 555-014-7702</li>
        <li><span class="contact__label">Phone:</span> 555-018-4419</li>
        <li><span class="contact__label">Email:</span> colby@marchettilaw.com</li>
        <li><span class="contact__label">Web:</span> www.marchettilaw.com</li>
        <li><span class="contact__label">Address:</span> 118B Harbor Avenue</li>
        <li>Bay Point, Florida 33001</li>
      </ul>
    </div>
  </section>
</body>
</html>
```